Home care agency

Current website QRVCAREPLUS.com. Need to update and reformat to different pages. use my info from my current website

Target Market(s)

adult children

Industry/Entity Type

Home Health

Coding

Coded - Design and coding required

Number of Pages Required

4 page

Font styles to use
Sans Serif

Colors
3276b5
33a6d7
3277b5
85cae6
85acd3

```html
<!DOCTYPE html>
<html lang="en">
<head>
<meta charset="utf-8">
<title>Seaside Haven Health Services – About</title>
<link href="https://fonts.googleapis.com/css2?family=Poppins:wght@300;400;700;800&display=swap" rel="stylesheet">
<style>
  :root {
    --brand-blue: #3276b5;
    --sky: #85cae6;
    --accent: #33a6d7;
    --soft-blue: #85acd3;
    --ink: #262626;
    --white: #ffffff;
  }
  * { margin: 0; padding: 0; box-sizing: border-box; }
  html, body { width: 1200px; height: 853px; overflow: hidden; background: var(--white); }
  body { font-family: "Poppins", sans-serif; color: var(--ink); position: relative; }

  .site-header { position: absolute; top: 0; left: 0; width: 1200px; height: 158px; }
  .brand { position: absolute; left: 100px; top: 66px; display: flex; align-items: center; gap: 10px; }
  .brand-dot { width: 22px; height: 22px; border-radius: 50%; background: var(--sky); }
  .brand-name { font-size: 17px; font-weight: 400; color: var(--brand-blue); }

  .main-nav { position: absolute; top: 70px; left: 0; width: 1200px; }
  .nav-link { position: absolute; font-size: 23px; font-weight: 400; color: var(--ink); text-decoration: none; line-height: 1; }
  .nav-link.is-active { color: var(--brand-blue); }
  .nav-link.is-active::after { content: ""; position: absolute; left: -5px; right: -6px; top: 34px; height: 4px; background: var(--brand-blue); }
  .nav-about { left: 700px; }
  .nav-services { left: 834px; }
  .nav-contact { left: 996px; }

  .hero { position: absolute; top: 158px; left: 0; width: 1200px; height: 205px; background: var(--sky); }
  .hero-title { position: absolute; left: 158px; top: 42px; font-size: 34px; font-weight: 800; line-height: 36px; color: var(--white); letter-spacing: -0.3px; }
  .hero-tagline { position: absolute; left: 158px; top: 134px; font-size: 22px; font-weight: 300; color: var(--white); }
  .hero-photo { position: absolute; left: 834px; top: 0; width: 366px; height: 205px;
    background: linear-gradient(120deg, #8a8176 0%, #b7aea3 45%, #e8e4de 60%, #6b5a4c 100%); }

  .about { position: absolute; top: 363px; left: 0; width: 1200px; height: 490px; }
  .about-heading { position: absolute; top: 55px; width: 1200px; text-align: center; font-size: 31px; font-weight: 400; }
  .about-copy { position: absolute; left: 118px; top: 142px; width: 690px; font-size: 16.6px; line-height: 21.7px; font-weight: 400; }
  .about-copy p + p { margin-top: 21.7px; }
  .about-copy a { color: var(--brand-blue); text-decoration: none; }
  .owner-portrait { position: absolute; left: 874px; top: 159px; width: 216px; height: 216px; border-radius: 50%;
    border: 9px solid var(--sky);
    background: radial-gradient(circle at 50% 45%, #efe9e0 0%, #cfc6ba 50%, #5c4d5e 100%); }
</style>
</head>
<body>
  <header class="site-header">
    <div class="brand">
      <span class="brand-dot"></span>
      <span class="brand-name">Seaside Haven</span>
    </div>
    <nav class="main-nav">
      <a class="nav-link nav-about is-active" href="#about">About</a>
      <a class="nav-link nav-services" href="#services">Services</a>
      <a class="nav-link nav-contact" href="#contact">Contact</a>
    </nav>
  </header>

  <section class="hero">
    <h1 class="hero-title">Seaside Haven Health<br>Services</h1>
    <p class="hero-tagline">Providing Care Throughout the South Shore</p>
    <div class="hero-photo" role="img" aria-label="Nurse in a white coat greeting a seated older man in a living room"></div>
  </section>

  <section class="about" id="about">
    <h2 class="about-heading">About</h2>
    <div class="about-copy">
      <p>Seaside Haven Health Services is owned and operated by Marissa Delcourt. Marissa is a registered nurse and has been in the health care system since 2001. She has specialized in home care, cardiology, trauma and critical care. She invests in future caregivers and has taught for the nursing programs at <a href="#">Bayview University,</a> CHI-HP, and <a href="#">Saint Aldric College</a>.</p>
      <p>All Seaside Haven caregivers have extensive background checks and training regarding HIPAA compliance. We individualize the care of our clients in order to provide the best care possible in their home. Seaside Haven also ensures full access and understanding of client care at all times with a caregiver binder in the client's home at all times. This binder includes information on the client’s care plan along and the notes from their caregivers. This will allow all caregivers and the client’s family to have an understanding of the care being provided.</p>
    </div>
    <div class="owner-portrait" role="img" aria-label="Portrait of the owner, a nurse in a white coat, seated in a chair"></div>
  </section>
</body>
</html>
```